Tobin Quartz Portal Page . It's guarantee project!

We need a clean and professional modern web application portal page
That includes the Login & Application Selection screen

Also, I need to design both Desktop and Mobile sizes.
We have an example design for our target

The application is Jetty Schedule and related data.
Our client is a bit conservative.

Theme color preferred : #00508B (main) #DF0D83 (secondary)

Target Market(s)

Oil & Fuel & Gasoline

Number of Pages Required

2 page

Font styles to use
Sans Serif

Colors
0054AA
0677BA
7BADD7
CADEEF
E8F1F8
E54698
E96AAD
F1A4CE
F9D9EA
FCEFF6

Requirements
Must have
• Login Page & Main Screen

```html
<!DOCTYPE html>
<html lang="en">
<head>
<meta charset="utf-8">
<title>Tobin Quartz Portal – Login &amp; Application Selection</title>
<link rel="stylesheet" href="https://fonts.googleapis.com/css2?family=Manrope:wght@400;500;600;700;800&display=swap">
<style>
:root{
  --stage:#1c1c1c;
  --blue:#0054aa;
  --blue-deep:#00508b;
  --pink:#df0d83;
  --pink-soft:#f9d9ea;
  --ice:#e8f1f8;
  --mist:#cadeef;
  --photo-a:#d3e3f1;
  --photo-b:#b7c9da;
  --ink:#1e2430;
  --ink-soft:#4a5160;
  --line:#c9cdd4;
  --hint:#b4b9c2;
  --white:#ffffff;
}
*{box-sizing:border-box;margin:0;padding:0}
html,body{width:887px;height:1200px;overflow:hidden;background:var(--stage);font-family:"Manrope",sans-serif;color:var(--ink)}
.board{position:absolute;overflow:hidden;background:var(--white)}
.photo{position:absolute;background:linear-gradient(180deg,var(--photo-a) 0%,#c6d7e7 55%,var(--photo-b) 100%)}
.abs{position:absolute}

/* brand lockup */
.brand{position:absolute;display:flex;align-items:center;gap:.35em;color:var(--blue);font-weight:800;white-space:nowrap;letter-spacing:-.01em}
.brand__mark{width:.9em;height:.9em;background:var(--pink);flex:none}

/* form parts */
.label{position:absolute;color:var(--ink);font-weight:500}
.field{position:absolute;border:1px solid var(--line);background:var(--white);color:var(--hint);display:flex;align-items:center}
.btn{position:absolute;display:flex;align-items:center;justify-content:center;color:var(--white);font-weight:500}
.btn--blue{background:var(--blue)}
.btn--pink{background:var(--pink)}
.link{position:absolute;color:var(--ink-soft);white-space:nowrap}
.link b{color:var(--blue);font-weight:700}

/* large desktop login */
.desk-lg{left:40px;top:40px;width:817px;height:580px}
.desk-lg .photo{left:0;top:0;width:380px;height:580px;border-top-right-radius:27px}
.desk-lg .brand{left:558px;top:170px;font-size:25px}
.desk-lg .label{font-size:12.5px}
.desk-lg .field{left:511px;width:257px;height:37px;border-radius:6px;padding-left:11px;font-size:10px}
.desk-lg .btn{left:511px;top:451px;width:257px;height:37px;border-radius:6px;font-size:12.5px}
.desk-lg .link{top:503px;font-size:10px}

/* small desktop boards */
.desk-sm{top:631px;width:268px;height:190px}
.desk-sm .photo{left:0;top:0;width:125px;height:190px;border-top-right-radius:10px}
.desk-sm .brand{font-size:9px}
.desk-sm .btn{border-radius:2px;font-size:4px}
.desk-sm .label{font-size:3.5px}
.desk-sm .field{left:154px;width:86px;height:12px;border-radius:2px;padding-left:4px;font-size:3px}
.desk-sm .link{font-size:3px}
.desk-a{left:39px}
.desk-b{left:313px}

/* desktop app chooser */
.desk-home{left:586px;top:631px;width:269px;height:190px;background:linear-gradient(160deg,#fbfcfe 20%,var(--ice) 60%,var(--mist) 100%)}
.desk-home .photo{left:0;top:0;width:56px;height:190px;border-top-right-radius:10px}
.greet{position:absolute;display:flex;align-items:center;gap:.5em;font-weight:600;color:var(--ink)}
.avatar{border-radius:50%;background:var(--mist);border:1.5px solid var(--blue);flex:none}
.signout{position:absolute;color:var(--blue);font-weight:600}
.title{position:absolute;font-weight:700;line-height:1.2;color:var(--ink)}
.tile{position:absolute;background:var(--white);border-radius:3px;box-shadow:0 1px 4px rgba(0,84,170,.12);display:flex;flex-direction:column;align-items:center;text-align:center;color:var(--ink);font-weight:600}
.tile--active{background:var(--pink);color:var(--white)}
.tile svg{color:var(--pink)}
.tile--active svg{color:var(--white)}
.desk-home .greet{left:84px;top:16px;font-size:4.5px}
.desk-home .avatar{width:13px;height:13px}
.desk-home .signout{right:18px;top:19px;font-size:4.5px}
.desk-home .title{left:85px;top:48px;font-size:9.5px}
.desk-home .tile{top:77px;width:46px;height:55px;padding-top:9px;font-size:3.8px;line-height:1.25}
.desk-home .tile svg{width:19px;height:19px;margin-bottom:4px}
.bar{position:absolute;background:var(--blue);display:flex;align-items:center}
.desk-home .bar{left:0;bottom:0;width:269px;height:24px;border-top-left-radius:10px;padding:0 16px}
.desk-home .bar .brand{position:static;color:var(--white);font-size:6px}
.desk-home .bar .brand__mark{background:var(--white)}
.chip{position:absolute;display:flex;align-items:center;gap:.35em;border-radius:3px;font-weight:600}
.chip--ghost{border:1px solid var(--white);color:var(--white)}
.chip--solid{background:var(--white);color:var(--blue)}
.chip svg{flex:none}
.desk-home .chip{top:7px;height:10px;padding:0 3px;font-size:4.3px}
.desk-home .chip svg{width:5px;height:5px}

/* mobile boards */
.mob{top:836px;width:154px;height:332px}
.mob > .photo{inset:0;width:auto;height:auto}
.mob-1{left:38px}.mob-2{left:204px}.mob-3{left:369px}.mob-4{left:535px}.mob-5{left:700px}
.mob .btn{left:16px;width:122px;border-radius:3px;font-size:6.5px}
.mob .sheet{position:absolute;left:0;right:0;bottom:0;background:rgba(241,244,248,.88);border-top-left-radius:14px;border-top-right-radius:14px}
.mob .label{left:16px;font-size:5.6px}
.mob .field{left:16px;width:122px;height:17px;border-radius:3px;padding-left:7px;font-size:3.6px}
.mob .link{font-size:3.6px}
.mob-1 .brand{left:27px;top:96px;font-size:13px}
.mob-2 .brand,.mob-3 .brand{left:34px;font-size:13px}
.mob-2 .brand{top:58px}
.mob-3 .brand{top:45px}

/* mobile app chooser */
.mob-home{background:linear-gradient(180deg,#fbfcfe 0%,var(--ice) 55%,var(--mist) 100%)}
.mob-home .greet{left:16px;top:21px;font-size:5.3px}
.mob-home .avatar{width:15px;height:15px}
.mob-home .signout{right:15px;top:26px;font-size:5.3px}
.mob-home .title{left:16px;top:60px;font-size:12px}
.row{position:absolute;left:16px;width:122px;height:47px;border-radius:8px;background:var(--white);box-shadow:0 1px 5px rgba(0,84,170,.1);display:flex;align-items:center;gap:12px;padding-left:10px;font-size:7.6px;font-weight:600;line-height:1.3;color:var(--ink)}
.row svg{width:27px;height:27px;color:var(--pink);flex:none}
.row--active{background:var(--pink);color:var(--white)}
.row--active svg{color:var(--white)}
.mob-home .bar{left:0;bottom:0;width:154px;height:38px;border-top-left-radius:14px;border-top-right-radius:14px}
.mob-home .chip{top:12px;height:15px;padding:0 5px;font-size:7px}
.mob-home .chip svg{width:8px;height:8px}
</style>
</head>
<body>

<svg width="0" height="0" style="position:absolute" aria-hidden="true">
  <symbol id="ico-training" viewBox="0 0 32 32" fill="none" stroke="currentColor" stroke-width="1.4" stroke-linecap="round" stroke-linejoin="round">
    <rect x="3" y="4" width="26" height="18" rx="1.5"/><path d="M12 22v4M20 22v4M9 27h14"/>
    <rect x="7" y="8" width="7" height="9"/><circle cx="10.5" cy="11" r="1.5"/><path d="M8.5 15.5c.5-1.5 3.5-1.5 4 0M17 9h8v5h-8zM17 17h8"/>
  </symbol>
  <symbol id="ico-performance" viewBox="0 0 32 32" fill="none" stroke="currentColor" stroke-width="1.4" stroke-linecap="round" stroke-linejoin="round">
    <rect x="3" y="4" width="26" height="18" rx="1.5"/><path d="M12 22v4M20 22v4M9 27h14"/>
    <rect x="7" y="7.5" width="18" height="11"/><path d="M9 16l4-4 3 2.5 6-5M19 9.5h3v3"/>
  </symbol>
  <symbol id="ico-tracking" viewBox="0 0 32 32" fill="none" stroke="currentColor" stroke-width="1.4" stroke-linecap="round" stroke-linejoin="round">
    <rect x="3" y="4" width="26" height="18" rx="1.5"/><path d="M12 22v4M20 22v4M9 27h14"/>
    <circle cx="10" cy="17" r="1.6"/><circle cx="22" cy="10" r="1.6"/><path d="M11.6 17H20a2.5 2.5 0 000-5h-6a2.5 2.5 0 010-5h6"/>
  </symbol>
  <symbol id="ico-home" viewBox="0 0 12 12" fill="none" stroke="currentColor" stroke-width="1.2" stroke-linejoin="round"><path d="M1.5 6L6 2l4.5 4M3 5v5h6V5"/></symbol>
  <symbol id="ico-done" viewBox="0 0 12 12" fill="none" stroke="currentColor" stroke-width="1.2" stroke-linecap="round" stroke-linejoin="round"><circle cx="6" cy="6" r="4.8"/><path d="M4 6.2l1.4 1.4L8.2 4.8"/></symbol>
</svg>

<!-- Desktop login, large -->
<section class="board desk-lg">
  <div class="photo" role="img" aria-label="Offshore jack-up drilling rigs standing in misty sea haze"></div>
  <div class="brand"><span class="brand__mark"></span>Tobin Quartz</div>
  <label class="label" style="left:511px;top:286px">Email</label>
  <div class="field" style="top:308px">youremailhere@mailbox.com</div>
  <label class="label" style="left:511px;top:363px">Password</label>
  <div class="field" style="top:385px">password</div>
  <div class="btn btn--blue">Sign In</div>
  <span class="link" style="left:511px">Create an account</span>
  <span class="link" style="left:692px">Forget Password</span>
</section>

<!-- Desktop welcome -->
<section class="board desk-sm desk-a">
  <div class="photo" role="img" aria-label="Offshore jack-up drilling rigs in haze"></div>
  <div class="brand" style="left:163px;top:54px"><span class="brand__mark"></span>Tobin Quartz</div>
  <div class="btn btn--blue" style="left:149px;top:105px;width:89px;height:12px">Sign In</div>
  <div class="btn btn--pink" style="left:149px;top:122px;width:89px;height:12px">Create an account</div>
</section>

<!-- Desktop login, small -->
<section class="board desk-sm desk-b">
  <div class="photo" role="img" aria-label="Offshore jack-up drilling rigs in haze"></div>
  <div class="brand" style="left:167px;top:44px"><span class="brand__mark"></span>Tobin Quartz</div>
  <label class="label" style="left:154px;top:80px">Email</label>
  <div class="field" style="top:86px">youremailhere@mailbox.com</div>
  <label class="label" style="left:154px;top:106px">Password</label>
  <div class="field" style="top:112px">password</div>
  <div class="btn btn--blue" style="left:154px;top:134px;width:86px;height:12px">Sign In</div>
  <span class="link" style="left:154px;top:150px">Create an account</span>
  <span class="link" style="left:215px;top:150px">Forget Password</span>
</section>

<!-- Desktop application chooser -->
<section class="board desk-home">
  <div class="photo" role="img" aria-label="Offshore jack-up drilling rigs in haze"></div>
  <div class="greet"><span class="avatar"></span>Hi, John Doe</div>
  <span class="signout">Sign Out</span>
  <h2 class="title">Choose an<br>Application</h2>
  <div class="tile" style="left:86px"><svg><use href="#ico-training"/></svg>Jetty<br>Training</div>
  <div class="tile tile--active" style="left:139px"><svg><use href="#ico-performance"/></svg>Jetty Port<br>Performance</div>
  <div class="tile" style="left:192px"><svg><use href="#ico-tracking"/></svg>Jetty<br>Tracking</div>
  <footer class="bar">
    <div class="brand"><span class="brand__mark"></span>Tobin Quartz</div>
    <span class="chip chip--ghost" style="left:181px"><svg><use href="#ico-home"/></svg>Home</span>
    <span class="chip chip--solid" style="left:215px"><svg><use href="#ico-done"/></svg>Done</span>
  </footer>
</section>

<!-- Mobile welcome -->
<section class="board mob mob-1">
  <div class="photo" role="img" aria-label="Offshore jack-up drilling rigs in haze"></div>
  <div class="brand"><span class="brand__mark"></span>Tobin Quartz</div>
  <div class="btn btn--blue" style="top:201px;height:17px">Sign In</div>
  <div class="btn btn--pink" style="top:225px;height:17px">Create an account</div>
</section>

<!-- Mobile sign in -->
<section class="board mob mob-2">
  <div class="photo" role="img" aria-label="Offshore jack-up drilling rigs in haze"></div>
  <div class="brand"><span class="brand__mark"></span>Tobin Quartz</div>
  <div class="sheet" style="top:142px"></div>
  <label class="label" style="top:173px">Email</label>
  <div class="field" style="top:182px">youremailhere@mailbox.com</div>
  <label class="label" style="top:209px">Password</label>
  <div class="field" style="top:218px">password</div>
  <div class="btn btn--blue" style="top:249px;height:17px">Sign In</div>
  <span class="link" style="left:16px;top:276px">Don't have an account? <b>Sign Up</b></span>
  <span class="link" style="left:103px;top:276px">Forget Password</span>
</section>

<!-- Mobile sign up -->
<section class="board mob mob-3">
  <div class="photo" role="img" aria-label="Offshore jack-up drilling rigs in haze"></div>
  <div class="brand"><span class="brand__mark"></span>Tobin Quartz</div>
  <div class="sheet" style="top:117px"></div>
  <label class="label" style="top:148px">Full Name</label>
  <div class="field" style="top:157px">Johnathan Doe</div>
  <label class="label" style="top:185px">Email</label>
  <div class="field" style="top:195px">emailaddress@mailbox.com</div>
  <label class="label" style="top:222px">Password</label>
  <div class="field" style="top:232px">••••••••••••••••</div>
  <div class="btn btn--blue" style="top:262px;height:18px">Sign Up</div>
  <span class="link" style="left:16px;top:290px">Already have an account? <b>Sign In</b></span>
</section>

<!-- Mobile application chooser -->
<section class="board mob mob-home mob-4">
  <div class="greet"><span class="avatar"></span>Hi, John Doe</div>
  <span class="signout">Sign Out</span>
  <h2 class="title">Choose an<br>Application</h2>
  <div class="row" style="top:108px"><svg><use href="#ico-training"/></svg>Jetty<br>Training</div>
  <div class="row" style="top:166px"><svg><use href="#ico-performance"/></svg>Jetty Port<br>Performance</div>
  <div class="row" style="top:225px"><svg><use href="#ico-tracking"/></svg>Jetty<br>Tracking</div>
  <footer class="bar">
    <span class="chip chip--ghost" style="left:16px"><svg><use href="#ico-home"/></svg>Home</span>
    <span class="chip chip--ghost" style="left:98px"><svg><use href="#ico-done"/></svg>Done</span>
  </footer>
</section>

<!-- Mobile application chooser, selected -->
<section class="board mob mob-home mob-5">
  <div class="greet"><span class="avatar"></span>Hi, John Doe</div>
  <span class="signout">Sign Out</span>
  <h2 class="title">Choose an<br>Application</h2>
  <div class="row" style="top:108px"><svg><use href="#ico-training"/></svg>Jetty<br>Training</div>
  <div class="row row--active" style="top:166px"><svg><use href="#ico-performance"/></svg>Jetty Port<br>Performance</div>
  <div class="row" style="top:225px"><svg><use href="#ico-tracking"/></svg>Jetty<br>Tracking</div>
  <footer class="bar">
    <span class="chip chip--ghost" style="left:16px"><svg><use href="#ico-home"/></svg>Home</span>
    <span class="chip chip--solid" style="left:98px"><svg><use href="#ico-done"/></svg>Done</span>
  </footer>
</section>

</body>
</html>
```